quiet meadow therapy (QMT)

I need to build a website for my therapy business.
There are two parts to the website
on the landing page; they choose whether they are therapists making a referral or patients needing more information.
After that, they are taken to their respective pages.
There is the textual information and a referral form on the therapist page, and on the patient page, the text is a bit different, and there will be a booking page on the patient page.
Visually minimal, it's a therapeutic website. I want it clean, clinical, and modern
colors: greenish blue or maybe orangish
PHP/html code
Updates

Hi everyone
I'm very sorry for the lack of responses to your designs. I am trying to work it out, but this platform has been a challenge for me.
I appreciate everyone's efforts, and I am unsure how to rate designs and move forward with the ones I like. There is a 5-star rating, but I don't understand how I'm supposed to politely say that it is not it without feeling like I'm going to affect someone's future rating negatively.
Please understand me. Thank you

Designs look the same

Target Market(s)

therapy and stress management

Industry/Entity Type

stress management therapy

Coding

Coded - Design and coding required

Number of Pages Required

5+ page

Font styles to use
Serif

Colors
0094D4
00A9DD
6FCCEA
C7EBF8
E9F6FB
00AB8E
00BBA5
67D7C9
C6EFE9
E9F9F6

Requirements
Must have
• landing page that that have 2 options. one for therapist another for patient

```html
<!DOCTYPE html>
<html lang="en">
<head>
<meta charset="utf-8">
<title>Quiet Meadow Therapy — Choose your path</title>
<link rel="stylesheet" href="https://fonts.googleapis.com/css2?family=Montserrat:wght@400;600&display=swap">
<style>
  :root {
    --teal: #0fb3a0;
    --ink: #1f1f1f;
    --muted: #6b6b6b;
    --white: #ffffff;
  }
  * { box-sizing: border-box; margin: 0; padding: 0; }
  html, body { width: 1200px; height: 675px; overflow: hidden; background: var(--white); }
  .landing {
    position: relative;
    width: 1200px;
    height: 675px;
    overflow: hidden;
    background: var(--white);
    font-family: "Montserrat", sans-serif;
  }
  .portrait {
    position: absolute;
    top: -79.5px;
    width: 834px;
    height: 834px;
    border-radius: 50%;
  }
  .portrait--therapist {
    left: -234px;
    background:
      linear-gradient(90deg, #6f7476 0 9%, transparent 14%),
      radial-gradient(circle at 52% 38%, #e6eef2 0 20%, transparent 45%),
      linear-gradient(180deg, #f3f6f7 0%, #dfe5e7 45%, #cdc8c0 70%, #b9b2a8 100%);
  }
  .portrait--patient {
    left: 600px;
    background:
      radial-gradient(circle at 25% 20%, #b4d6d3 0 30%, transparent 60%),
      linear-gradient(180deg, #a8cfcb 0%, #8ebdbb 35%, #3b5f86 55%, #2d4c72 100%);
  }
  .choice {
    position: absolute;
    top: 302px;
    height: 75px;
    display: flex;
    align-items: center;
    justify-content: center;
    text-decoration: none;
    font-weight: 600;
    font-size: 27px;
    letter-spacing: 0.2px;
  }
  .choice svg { position: absolute; inset: 0; width: 100%; height: 100%; }
  .choice span { position: relative; }
  .choice--therapist { left: 160px; width: 323px; color: var(--white); padding-right: 46px; }
  .choice--patient { left: 721px; width: 318px; color: var(--teal); padding-left: 48px; }
  .brand {
    position: absolute;
    left: 0;
    right: 0;
    top: 30px;
    display: flex;
    justify-content: center;
    align-items: center;
    gap: 10px;
  }
  .brand__dot {
    width: 18px;
    height: 18px;
    border-radius: 50%;
    background: var(--teal);
  }
  .brand__name {
    font-weight: 600;
    font-size: 20px;
    color: var(--ink);
    line-height: 1;
  }
  .legal {
    position: absolute;
    left: 0;
    right: 0;
    top: 631px;
    text-align: center;
    font-size: 12px;
    line-height: 18px;
    color: var(--muted);
  }
</style>
</head>
<body>
<main class="landing">
  <div class="portrait portrait--therapist" role="img" aria-label="Photo of a smiling therapist seated in an armchair holding a clipboard"></div>
  <div class="portrait portrait--patient" role="img" aria-label="Photo of a calm patient in a striped cardigan seated on a blue sofa"></div>

  <a class="choice choice--therapist" href="#therapist">
    <svg viewBox="0 0 323 75" preserveAspectRatio="none" aria-hidden="true">
      <path d="M0 0 H276 L323 37.5 L276 75 H0 Z" fill="var(--teal)"/>
    </svg>
    <span>FOR THERAPIST</span>
  </a>

  <a class="choice choice--patient" href="#patient">
    <svg viewBox="0 0 318 75" preserveAspectRatio="none" aria-hidden="true">
      <path d="M48 0 H318 V75 H48 L0 37.5 Z" fill="var(--white)"/>
    </svg>
    <span>FOR PATIENT</span>
  </a>

  <header class="brand">
    <span class="brand__dot"></span>
    <span class="brand__name">Quiet Meadow Therapy</span>
  </header>

  <footer class="legal">© 2022 Quiet Meadow Therapy.<br>All Rights Reserved.</footer>
</main>
</body>
</html>
```